A Maple Syrup Label for a Local Buniness

We are looking for a label for our maple syrup business. Our business currently sells honey, and we are expanding into maple syrup. Our Business name is "Brackley Honey" and we currently have a logo attached below. We would like to incorporate the bee and BH part, but the label could also read "Brackley Farms" with the words maple syrup. We do not want consumers to confuse the maple syrup jars with the honey jars. It should be clear that the jars contain maple syrup. We are open to new designs as well.

```html
<!DOCTYPE html>
<html lang="en">
<head>
<meta charset="utf-8">
<title>Brackley Honey &amp; Farms – Maple Syrup Label</title>
<link rel="stylesheet" href="https://fonts.googleapis.com/css2?family=Libre+Baskerville&family=Open+Sans:wght@700&display=swap">
<style>
  :root {
    --page-bg: #e4e4e4;
    --label-cream: #f9e7cc;
    --ink-black: #181512;
    --honey-gold: #f4bb14;
    --maple-red: #9d2822;
    --band-red: #97221e;
    --leaf-orange: #e07a2a;
    --leaf-amber: #e6a338;
    --leaf-rust: #b84a24;
    --text-white: #fdf6ee;
  }
  * { margin: 0; padding: 0; box-sizing: border-box; }
  html, body {
    width: 1000px;
    height: 1200px;
    overflow: hidden;
    background: var(--page-bg);
  }
  .label {
    position: absolute;
    left: 20px;
    top: 325px;
    width: 960px;
    height: 549px;
    background: var(--label-cream);
    overflow: hidden;
  }
  .leaf-border {
    position: absolute;
  }
  .leaf-border--top {
    left: 0; top: 0; width: 100%; height: 70px;
    background: linear-gradient(180deg, rgba(224,122,42,.75), rgba(230,163,56,.35) 60%, rgba(249,231,204,0));
  }
  .leaf-border--bottom {
    left: 0; bottom: 0; width: 100%; height: 95px;
    background: linear-gradient(0deg, rgba(184,74,36,.75), rgba(230,163,56,.4) 60%, rgba(249,231,204,0));
  }
  .leaf-border--left {
    left: 0; top: 0; width: 170px; height: 100%;
    background: linear-gradient(90deg, rgba(224,122,42,.7), rgba(230,163,56,.35) 55%, rgba(249,231,204,0));
  }
  .leaf-border--right {
    right: 0; top: 0; width: 190px; height: 100%;
    background: linear-gradient(270deg, rgba(224,122,42,.7), rgba(230,163,56,.35) 55%, rgba(249,231,204,0));
  }
  .brand-mark {
    position: absolute;
    left: 0; top: 100px;
    width: 100%;
    display: flex;
    justify-content: center;
    align-items: center;
    gap: 12px;
  }
  .brand-mark__dot {
    width: 26px; height: 26px;
    border-radius: 50%;
    background: var(--honey-gold);
  }
  .brand-mark__name {
    font-family: "Libre Baskerville", serif;
    font-size: 26px;
    color: var(--ink-black);
  }
  .brand-title {
    position: absolute;
    left: 0; width: 100%;
    text-align: center;
    font-family: "Libre Baskerville", serif;
    font-size: 54px;
    line-height: 1;
    letter-spacing: 1px;
  }
  .brand-title--owner { top: 200px; color: var(--ink-black); }
  .brand-title--range { top: 258px; }
  .brand-title .honey { color: var(--honey-gold); }
  .brand-title .amp { color: var(--ink-black); }
  .brand-title .farms { color: var(--maple-red); }
  .product-band {
    position: absolute;
    left: 214px; top: 331px;
    width: 534px; height: 58px;
    background: linear-gradient(90deg, rgba(151,34,30,0) 0%, var(--band-red) 30%, var(--band-red) 70%, rgba(151,34,30,0) 100%);
    display: flex;
    align-items: center;
    justify-content: center;
  }
  .product-band__name {
    font-family: "Libre Baskerville", serif;
    font-size: 36px;
    color: var(--text-white);
  }
  .net-weight {
    position: absolute;
    left: 0; top: 412px; width: 100%;
    text-align: center;
    font-family: "Open Sans", sans-serif;
    font-weight: 700;
    font-size: 38px;
    color: var(--maple-red);
  }
</style>
</head>
<body>
  <main class="label">
    <div class="leaf-border leaf-border--top" role="img" aria-label="Scattered autumn maple leaves along the top edge"></div>
    <div class="leaf-border leaf-border--bottom" role="img" aria-label="Scattered autumn maple leaves along the bottom edge"></div>
    <div class="leaf-border leaf-border--left" role="img" aria-label="Scattered autumn maple leaves along the left edge"></div>
    <div class="leaf-border leaf-border--right" role="img" aria-label="Scattered autumn maple leaves along the right edge"></div>

    <div class="brand-mark">
      <span class="brand-mark__dot"></span>
      <span class="brand-mark__name">Brackley Honey</span>
    </div>

    <h1 class="brand-title brand-title--owner">BRACKLEY</h1>
    <p class="brand-title brand-title--range"><span class="honey">HONEY</span> <span class="amp">&amp;</span> <span class="farms">FARMS</span></p>

    <div class="product-band">
      <span class="product-band__name">Maple Syrup</span>
    </div>

    <p class="net-weight">500 gm</p>
  </main>
</body>
</html>
```